Modern luxury trendy cosmetics label

Looking for a cosmetics packaging label design. We are looking for a professionel, modern and luxury look like Lorena Vasquel, Meadowkin Apothecary, Marigold Tessin, Gavin Albert Pruke, Zuna, Orvik + Dalle, Velumi, Sleepy Walrus, the plainfold, lumiere de sable.Name of product: Nordic Tulip Mask - Needle-Free Contour Ritual Ingredients that have scientific proof of anti aging: Cherry blossom extact, collegen, hyaluronic acid, coconut oil. Color of product itself: Pastel pink. Smell: Cherry blossom. Colors of label: simple and black and white or some subtle colors.

Target Market(s)

Women, luxury market, modern women, young and old women

Industry/Entity Type

Cosmetics

Font styles to use
Sans Serif

Colors

Designer to choose colors to be used in the design.

Requirements
Must have
• A modern look, professional, cosmetics, beauty, professional market, original

```html
<!DOCTYPE html>
<html lang="en">
<head>
<meta charset="utf-8">
<title>Orlae — Nordic Tulip Mask Label</title>
<link rel="stylesheet" href="https://fonts.googleapis.com/css2?family=Josefin+Sans:wght@300;400&display=swap">
<style>
  :root {
    --label-black: #000000;
    --blossom-pink: #e6b3cf;
  }
  * { margin: 0; padding: 0; box-sizing: border-box; }
  html, body {
    width: 1002px;
    height: 1200px;
    overflow: hidden;
    background: var(--label-black);
  }
  .label {
    position: relative;
    width: 1002px;
    height: 1200px;
    background: var(--label-black);
    color: var(--blossom-pink);
    font-family: "Josefin Sans", sans-serif;
  }
  .label__frame {
    position: absolute;
    left: 128px;
    top: 190px;
    width: 756px;
    height: 837px;
    border: 9px solid var(--blossom-pink);
  }
  .label__content {
    position: absolute;
    left: 128px;
    top: 190px;
    width: 756px;
    height: 837px;
    text-align: center;
  }
  .brand-name {
    position: absolute;
    left: 0; right: 0;
    top: 66px;
    font-size: 66px;
    font-weight: 400;
    letter-spacing: 0.01em;
    line-height: 1;
  }
  .product-title {
    position: absolute;
    left: 0; right: 0;
    top: 200px;
    font-weight: 300;
    font-size: 94px;
    line-height: 119px;
    letter-spacing: 0.3em;
    padding-left: 0.3em;
  }
  .product-title span { display: block; }
  .product-claim {
    position: absolute;
    left: 0; right: 0;
    top: 608px;
    font-size: 26px;
    font-weight: 400;
    letter-spacing: 0.2em;
    padding-left: 0.2em;
  }
  .ingredients {
    position: absolute;
    left: 40px; right: 40px;
    top: 710px;
    font-size: 15.5px;
    font-weight: 400;
    line-height: 28px;
    letter-spacing: 0.16em;
  }
</style>
</head>
<body>
  <main class="label">
    <div class="label__frame"></div>
    <div class="label__content">
      <p class="brand-name">orlae</p>
      <h1 class="product-title">
        <span>NORDIC</span>
        <span>TULIP</span>
        <span>MASK</span>
      </h1>
      <p class="product-claim">NEEDLE-FREE CONTOUR RITUAL</p>
      <p class="ingredients">MADE WITH ANTI-AGING INGREDIENTS: CHERRY BLOSSOM<br>EXTACT, COLLEGEN, HYALURONIC ACID, COCONUT OIL</p>
    </div>
  </main>
</body>
</html>
```